Masonry and Landscaping Construction company business card

Looking for a business card design for a construction company named Ferrano Construction. It is an italian-american family business that specializes in custom stone work, patios, walkways, driveways, steps, outdoor kitchens, concrete, waterproofing, power wash, landscaping and more. Our colors are mostly red and white with some black. We're looking for a bold design. we also like to incorporate a picture of my family's hometown somewhere in it.
Target Market(s)
Luxury home owners
Industry/Entity Type
Construction
Contact Information for Business Card
Details includes should be bullet points mentioning the services provided. Custom Stone Work, Outdoor Kitchens, Fire Pits, Patios, Walkways, Steps, Concrete, Waterproofing, powerwash and landscaping
Requirements
Must have
- Would like a spot on the card for co-owners names, numbers and email to be listed also looking to add the QR code for an instagram page
Nice to have
- would like something bold, based around the colors red and white with black outlines or details

```html
<!DOCTYPE html>
<html lang="en">
<head>
<meta charset="utf-8">
<title>Ferrano Construction – Business Card</title>
<link href="https://fonts.googleapis.com/css2?family=Montserrat:wght@500;700;800&family=Ubuntu:wght@400;500;700&display=swap" rel="stylesheet">
<style>
  :root {
    --red: #d71f27;
    --white: #ffffff;
    --ink: #1c1c1c;
    --stage: #b9b9b9;
    --photo-sky: #c9d3dc;
    --photo-green: #5f8d4a;
    --photo-stone: #b69a7e;
  }
  * { margin: 0; padding: 0; box-sizing: border-box; }
  html, body { width: 1200px; height: 815px; overflow: hidden; }
  body {
    background: var(--stage);
    font-family: "Ubuntu", sans-serif;
    position: relative;
  }
  .card {
    position: absolute;
    left: 320px;
    width: 560px;
    height: 320px;
    border-radius: 20px;
    overflow: hidden;
    box-shadow: 0 10px 24px rgba(0,0,0,0.28);
  }
  .card--front { top: 62px; background: var(--white); }
  .card--back  { top: 430px; background: var(--red); }

  /* Front */
  .front__art { position: absolute; inset: 0; width: 560px; height: 320px; }
  .front__tab {
    position: absolute; top: 0; right: 26px;
    width: 44px; height: 14px; background: var(--red);
    border-radius: 0 0 4px 4px;
  }
  .front__person {
    position: absolute; top: 26px; right: 112px; text-align: right;
  }
  .front__name {
    font-family: "Montserrat", sans-serif; font-weight: 700;
    font-size: 25px; letter-spacing: 0.5px; color: var(--red); line-height: 1;
  }
  .front__role {
    font-family: "Montserrat", sans-serif; font-weight: 500;
    font-size: 12px; letter-spacing: 1px; color: var(--ink); margin-top: 4px;
  }
  .wordmark {
    display: flex; align-items: center; gap: 10px;
    font-family: "Ubuntu", sans-serif; font-weight: 700; line-height: 1.05;
    text-transform: uppercase;
  }
  .wordmark__square { flex: none; }
  .front__wordmark {
    position: absolute; left: 40px; top: 104px;
    font-size: 24px; color: var(--ink);
  }
  .front__wordmark .wordmark__square { width: 18px; height: 18px; background: var(--red); }
  .front__contact {
    position: absolute; left: 110px; top: 212px;
    font-size: 16px; color: var(--ink);
    display: flex; flex-direction: column; gap: 12px;
  }
  .contact-line { display: flex; align-items: center; gap: 10px; }
  .contact-line svg { width: 16px; height: 16px; flex: none; }

  /* Back */
  .back__wordmark {
    position: absolute; left: 0; right: 0; top: 96px;
    justify-content: center; font-size: 36px; color: var(--white);
  }
  .back__wordmark .wordmark__square { width: 24px; height: 24px; background: var(--white); }
  .back__services {
    position: absolute; left: 30px; right: 30px; bottom: 36px;
    text-align: center; color: var(--white);
    font-size: 14.5px; font-weight: 500; letter-spacing: 0.3px;
    text-transform: uppercase; line-height: 1.5;
  }
</style>
</head>
<body>

  <section class="card card--front">
    <svg class="front__art" viewBox="0 0 560 320">
      <defs>
        <linearGradient id="hometown" x1="0" y1="0" x2="0.6" y2="1">
          <stop offset="0" stop-color="var(--photo-sky)"/>
          <stop offset="0.35" stop-color="var(--photo-green)"/>
          <stop offset="0.7" stop-color="var(--photo-stone)"/>
          <stop offset="1" stop-color="var(--photo-green)"/>
        </linearGradient>
      </defs>
      <path d="M312 320 C 312 185, 420 92, 560 72 L 560 320 Z" fill="none" stroke="var(--red)" stroke-width="5"/>
      <path role="img" aria-label="Photo of the family's hometown: hillside Italian village with a church tower and green mountains"
            d="M326 320 C 326 195, 428 104, 560 86 L 560 320 Z" fill="url(#hometown)"/>
    </svg>

    <div class="front__tab"></div>
    <div class="front__person">
      <div class="front__name">PAOLO FERRANO</div>
      <div class="front__role">CO-OWNERS</div>
    </div>

    <div class="wordmark front__wordmark">
      <span class="wordmark__square"></span>
      <span>Ferrano<br>Construction</span>
    </div>

    <div class="front__contact">
      <div class="contact-line">
        <svg viewBox="0 0 24 24" aria-hidden="true"><path fill="var(--red)" d="M6.6 10.8a15.1 15.1 0 0 0 6.6 6.6l2.2-2.2c.3-.3.7-.4 1-.2 1.1.4 2.3.6 3.6.6.6 0 1 .4 1 1V20c0 .6-.4 1-1 1A17 17 0 0 1 3 4c0-.6.4-1 1-1h3.5c.6 0 1 .4 1 1 0 1.3.2 2.5.6 3.6.1.3 0 .7-.2 1z"/></svg>
        <span>(555)318-4427</span>
      </div>
      <div class="contact-line">
        <svg viewBox="0 0 24 24" aria-hidden="true"><rect x="2" y="5" width="20" height="14" rx="2" fill="var(--red)"/><path d="M3 6l9 7 9-7" fill="none" stroke="var(--white)" stroke-width="2"/></svg>
        <span>info@ferranobuild.com</span>
      </div>
    </div>
  </section>

  <section class="card card--back">
    <div class="wordmark back__wordmark">
      <span class="wordmark__square"></span>
      <span>Ferrano<br>Construction</span>
    </div>
    <p class="back__services">
      Custom stone work, outdoor kitchens, fire pits, patios, walkways,<br>
      steps, concrete, waterproofing, powerwash and landscaping
    </p>
  </section>

</body>
</html>
```